Copper Ridge Garage Door Sales & Repair needs a Business Card Design

I need a business card design to go with our new business logo that was created a few months ago.

Copper Ridge Garage Door specializes in selling and installing new garage doors, and new garage door openers. We also take care of all repairs to existing garage doors and garage door openers. All makes and models.

Target Market(s)

Home-owners, renters, anyone who lives in a house and has a garage. Residential and commercial garages.

Industry/Entity Type

Home Improvement

Contact Information for Business Card

I would like the business cards to have rounded corners and be double-sided. My old logo is still on my website at www.copperridgegarage.example. If I was going to incorporate a secondary color on the business cards, I think that orange is a good choice (especially since blue and orange are the colors of our Tulsa Kestrels), but I'm not opposed to seeing a different color if another color works better with my logo colors. I have two logo colors. One designed for a white background and one designed for a darker background. I'm not opposed to using both. Maybe a dark background with the white logo on one side, and a white background with the other logo color on the other side.

My business is a small, locally owned business that I am trying to grow. But I would like my business cards to look very professional. Like we have been in business for a long time. I like traditional to modern looking cards. Just something bold and memorable. My full company name is Copper Ridge Garage Door Sales & Repair. But you can just do COPPER RIDGE GARAGE DOOR, if that works better.

Font styles to use
Serif
Script

Requirements
Must have
• Rounded corners
• Double-sided
• 3-D Elements. Layering of some sort (a sketch of a garage door or a 3rd color (orange) brought in some how. I really like watermarks.
• Matte cards that you can write on.
• White on one side. (Or the lighter blue in my logo). Darker blue logo color on the other side.
• I would like our tag line on the cards somewhere... "For All Your Garage Door Needs".
• I would also like "Call For a FREE Estimate" by the phone number.
• And "Serving the Greater Metro Denver Area" somewhere on the card as well.
Nice to have
• Refer to "Business Card Details" above.

```html
<!DOCTYPE html>
<html lang="en">
<head>
<meta charset="utf-8">
<title>Copper Ridge Garage Door – Business Card</title>
<link href="https://fonts.googleapis.com/css2?family=Arimo:wght@400;700&family=Saira:wght@500&family=Roboto+Slab:wght@800&display=swap" rel="stylesheet">
<style>
  :root {
    --navy: #3f4f75;
    --navy-deep: #34426a;
    --white: #ffffff;
    --ink: #1d1f24;
    --stage: #e9e7e3;
    --ghost: rgba(255,255,255,0.07);
  }
  html, body { margin: 0; height: 100%; overflow: hidden; }
  body {
    width: 1200px; height: 892px;
    background: var(--stage);
    position: relative;
    font-family: "Arimo", Arial, sans-serif;
  }
  .card {
    position: absolute;
    top: 136px;
    width: 380px; height: 620px;
    border-radius: 26px;
    overflow: hidden;
    box-shadow: 0 10px 28px rgba(0,0,0,0.18);
  }
  .card--front { left: 180px; background: var(--white); }
  .card--back  { left: 640px; background: var(--navy); }

  /* front */
  .front__band {
    position: absolute; left: 0; top: 0; width: 100%; height: 240px;
    background: var(--navy);
  }
  .brand-seal {
    position: absolute; left: 50px; top: 90px;
    width: 280px; height: 280px; border-radius: 50%;
    background: var(--navy-deep);
    display: flex; align-items: center; justify-content: center;
    text-align: center;
  }
  .brand-name {
    font-family: "Roboto Slab", Georgia, serif;
    font-weight: 800;
    color: var(--white);
    font-size: 30px; line-height: 1.1;
    letter-spacing: 1px;
  }
  .person { position: absolute; left: 34px; right: 30px; top: 398px; text-align: right; }
  .person__name {
    font-family: "Saira", Arial, sans-serif; font-weight: 500;
    font-size: 34px; color: var(--navy); letter-spacing: 2px; line-height: 1;
  }
  .person__role {
    font-size: 21px; font-weight: 700; color: var(--ink); margin-top: 4px;
    letter-spacing: 0.5px;
  }
  .contact { position: absolute; left: 26px; top: 478px; list-style: none; margin: 0; padding: 0; }
  .contact li {
    display: flex; align-items: flex-start; gap: 8px;
    font-size: 16px; color: var(--ink); line-height: 21px;
  }
  .contact__icon {
    flex: none; width: 14px; height: 14px; margin-top: 3px;
    background: #3a3d44; border-radius: 2px;
    display: flex; align-items: center; justify-content: center;
  }
  .contact__icon svg { width: 10px; height: 10px; }

  /* back */
  .back__watermark {
    position: absolute; right: 22px; top: 210px; width: 170px;
    font-family: "Roboto Slab", Georgia, serif; font-weight: 800;
    color: var(--ghost); font-size: 28px; line-height: 1.15; text-align: center;
  }
  .back__stripe {
    position: absolute; top: 0; bottom: 0; left: 40px; width: 44px;
    background: var(--white);
  }
  .back__line {
    position: absolute; top: 150px;
    writing-mode: vertical-rl;
    white-space: nowrap;
  }
  .back__line--area {
    left: 40px; width: 44px; line-height: 44px;
    font-size: 19px; color: var(--navy);
  }
  .back__line--tag {
    left: 90px; width: 40px; line-height: 40px;
    font-size: 21px; color: var(--white);
  }
  .back__line--call {
    left: 132px; width: 46px; line-height: 46px;
    font-size: 26px; color: var(--white);
  }
</style>
</head>
<body>

<section class="card card--front" aria-label="Card front">
  <div class="front__band"></div>
  <div class="brand-seal">
    <div class="brand-name">COPPER RIDGE<br>GARAGE DOOR</div>
  </div>
  <div class="person">
    <div class="person__name">Dana Whitlock</div>
    <div class="person__role">Project Manager</div>
  </div>
  <ul class="contact">
    <li><span class="contact__icon"><svg viewBox="0 0 10 10"><path d="M2 1h2l1 2-1 1a5 5 0 0 0 2 2l1-1 2 1v2c-4 0-7-3-7-7z" fill="#fff"/></svg></span>303.555.0142</li>
    <li><span class="contact__icon"><svg viewBox="0 0 10 10"><rect x="1" y="2.5" width="8" height="5" fill="none" stroke="#fff"/><path d="M1 2.5l4 3 4-3" fill="none" stroke="#fff"/></svg></span>dana@copperridgegarage.example</li>
    <li><span class="contact__icon"><svg viewBox="0 0 10 10"><circle cx="5" cy="5" r="3.6" fill="none" stroke="#fff"/><path d="M1.4 5h7.2M5 1.4v7.2" stroke="#fff"/></svg></span>www.copperridgegarage.example</li>
    <li><span class="contact__icon"><svg viewBox="0 0 10 10"><path d="M5 9S2 5.6 2 3.8a3 3 0 0 1 6 0C8 5.6 5 9 5 9z" fill="#fff"/></svg></span>4200 Alpine Loop Suite 12,<br>Arvada, CO 80002</li>
  </ul>
</section>

<section class="card card--back" aria-label="Card back">
  <div class="back__watermark">COPPER RIDGE GARAGE DOOR</div>
  <div class="back__stripe"></div>
  <div class="back__line back__line--area">"Serving the Greater Metro Denver Area"</div>
  <div class="back__line back__line--tag">"For All Your Garage Door Needs"</div>
  <div class="back__line back__line--call">"Call For a FREE Estimate"</div>
</section>

</body>
</html>
```